Business card design needed

A small accounting firm that has relocated from the regional areas of Australia, to be city based, and using the resources of The Cloud to remake and streamline its operations, and wanting to share the benefits with small businesses all over Australia. We provide services on a fixed price basis, and run regular events for clients and potential clients.

Major product partners are Quorel Ledgering, Gatherloom, SlotFinch, Tallo and Pagemoss.

Please review the update to the brief.

Thanks.

Reason: Just swamped by good designs, need more time to provide feedback and make choices. Thanks in advance for the great efforts so far!

Need cards for 2 people

1. Dennis Halvorsen, Development Director
Mobile - 0499 572 438
dennis@fernbrookledger.example

2. Ruth Okonedo, Accountant
Mobile - 0488 164 729
ruth@fernbrookledger.example

Please check the amendments to the brief regarding web address etc.

Reason: Wanting some revisions before final selection.

Target Market(s)

Micro and Small business owners, trades, service and hospitality industries. Web savvy.

Industry/Entity Type

Accounting

Contact Information for Business Card

Fernbrook Ledger,
Level 5, Harwick Lane Plaza,
127 Harwick Lane, Melbourne, 3000

Logo Text

Fernbrook Ledger - Ledger Accounting and Business Solutions

Logo styles of interest
Abstract Logo
Requirements
Must have
• Must include some tagline for our services - eg Accounting & Business services, Fixed Price, Tax

On Reverse side
Twitter Address - @FernbrookLedgerAu
Facebook - www.socialpage.example/FernbrookLedger
Book Online Appointment (Slot Finch) - www.shortlink.example/ledgerslot
Nice to have
• The Quorel Logo - We are a Quorel Partner. Guidelines for logo use have been uploaded.

```html
<!DOCTYPE html>
<html lang="en">
<head>
<meta charset="utf-8">
<title>Fernbrook Ledger – Business Card</title>
<link rel="stylesheet" href="https://fonts.googleapis.com/css2?family=Montserrat:wght@400;500;600&family=Arimo&display=swap">
<style>
  :root {
    --sky: #00ffff;
    --white: #ffffff;
    --ink: #111111;
    --edge: #d4d4d4;
  }
  * { margin: 0; padding: 0; box-sizing: border-box; }
  html, body {
    width: 1200px;
    height: 1139px;
    overflow: hidden;
    background: var(--white);
  }
  .sheet {
    position: relative;
    width: 1200px;
    height: 1139px;
    font-family: "Montserrat", sans-serif;
  }
  .card {
    position: absolute;
    left: 38px;
    width: 863px;
    height: 486px;
    overflow: hidden;
  }
  .card--front { top: 45px; background: var(--sky); }
  .card--back {
    top: 614px;
    background: var(--white);
    border: 2px solid var(--edge);
  }
  .side-label {
    position: absolute;
    left: 1025px;
    font-family: "Arimo", sans-serif;
    font-size: 31px;
    color: var(--ink);
    line-height: 1;
  }
  .side-label--front { top: 290px; }
  .side-label--back { top: 832px; }

  .brand-dot {
    position: absolute;
    border-radius: 50%;
  }
  .card--front .brand-dot {
    left: 324px;
    top: 62px;
    width: 220px;
    height: 220px;
    background: radial-gradient(circle, var(--white) 0 62%, rgba(255,255,255,0) 72%);
  }
  .brand-name {
    position: absolute;
    left: 0;
    right: 0;
    top: 332px;
    text-align: center;
    font-weight: 600;
    font-size: 56px;
    letter-spacing: 0.2px;
    color: var(--white);
    line-height: 1;
  }
  .tagline {
    position: absolute;
    left: 0;
    right: 0;
    top: 412px;
    text-align: center;
    font-weight: 500;
    font-size: 18px;
    letter-spacing: 1px;
    color: var(--white);
    line-height: 1;
  }

  .card--back .brand-dot {
    left: 254px;
    top: 12px;
    width: 356px;
    height: 356px;
    background: radial-gradient(circle, var(--sky) 0 62%, rgba(0,255,255,0) 72%);
  }
  .contact {
    position: absolute;
    left: 0;
    right: 0;
    text-align: center;
    color: var(--white);
    line-height: 1;
  }
  .contact__name {
    top: 162px;
    font-weight: 600;
    font-size: 22px;
    letter-spacing: 1px;
  }
  .contact__phone {
    top: 213px;
    font-weight: 500;
    font-size: 16px;
    letter-spacing: 1px;
  }
  .contact__email {
    top: 240px;
    font-weight: 500;
    font-size: 16px;
  }
  .online {
    position: absolute;
    left: 0;
    right: 0;
    top: 386px;
    text-align: center;
    font-size: 13px;
    font-weight: 400;
    color: var(--sky);
    line-height: 1;
  }
  .address {
    position: absolute;
    left: 0;
    right: 0;
    top: 416px;
    text-align: center;
    font-size: 16px;
    font-weight: 400;
    color: var(--sky);
    letter-spacing: -0.2px;
    line-height: 1;
  }
</style>
</head>
<body>
<main class="sheet">
  <section class="card card--front" aria-label="Card front">
    <div class="brand-dot"></div>
    <h1 class="brand-name">Fernbrook Ledger</h1>
    <p class="tagline">Accounting &amp; Business Services • Fixed Price • Tax</p>
  </section>
  <p class="side-label side-label--front">FRONT</p>

  <section class="card card--back" aria-label="Card back">
    <div class="brand-dot"></div>
    <p class="contact contact__name">Dennis HALVORSEN</p>
    <p class="contact contact__phone">0499572438</p>
    <p class="contact contact__email">dennis@fernbrookledger.example</p>
    <p class="online">@FernbrookLedgerAu • www.socialpage.example/FernbrookLedger • Book online: www.shortlink.example/ledgerslot</p>
    <p class="address">Fernbrook Ledger • Level 5 Harwick Lane Plaza • 127 Harwick Lane • Melbourne 3000</p>
  </section>
  <p class="side-label side-label--back">BACK</p>
</main>
</body>
</html>
```